We need a new design for our construction website

We need a new website for our wordpress site kerrowmade.co.nz

It needs to be only a few pages but sleek in design and responsive, beautifully showcasing our images and video. Currently we have
1. home
2. about us
3. contact
We need either a front page that is designed much better to showcase more content, or potentially a projects page which has images from our builds. We don't have a lot of content so the content we do have needs to be maximised by image, rather than project.

Target Market(s)

High end residential construction and renovation projects, people wanting to build a nice home, clients based in Mount Maunganui, Tauranga.

Coding

Font styles to use
Sans Serif

Colors

Designer to choose only greyscale colors for use in the design.

Requirements
Must have
• A sleek design, architectural

```html
<!DOCTYPE html>
<html lang="en">
<head>
<meta charset="utf-8">
<title>Kerrowmade — Architectural Builders</title>
<link rel="stylesheet" href="https://fonts.googleapis.com/css2?family=Raleway:wght@400;500;700&family=Lato:wght@400;700&family=Mulish:wght@400;600&display=swap">
<style>
:root{
  --accent:#4a4a4a;
  --accent-light:#d6d6d6;
  --footer:#1f1f1f;
  --ink:#111111;
  --text:#333333;
  --muted:#9a9a9a;
  --panel:#f7f7f7;
  --panel-alt:#f4f4f4;
  --white:#ffffff;
  --page:#ffffff;
}
*{box-sizing:border-box;margin:0;padding:0}
html,body{width:768px;height:1200px;overflow:hidden;background:var(--page)}
body{position:relative;font-family:'Raleway',sans-serif;color:var(--ink)}
.site{position:absolute;left:102px;top:0;width:565px;height:1200px;overflow:hidden}
.abs{position:absolute}

/* hero */
.hero{left:0;top:0;width:565px;height:208px;overflow:hidden}
.hero-photo{left:0;top:0;width:565px;height:208px;background:linear-gradient(180deg,#6e6e6e 0%,#8a8a8a 30%,#3a3a3a 62%,#1c1c1c 80%,#555 100%)}
.brand{left:8px;top:8px;display:flex;align-items:center;gap:8px;color:var(--white);font-family:'Raleway',sans-serif;font-weight:400;font-size:11px;letter-spacing:4px}
.brand-dot{width:22px;height:22px;border:1.5px solid var(--white);border-radius:50%;flex:none}
.call{left:220px;top:14px;font-family:'Lato',sans-serif;font-weight:700;font-size:7px;color:var(--white)}
.hero-frame{left:145px;top:44px;width:127px;height:143px;border:2px solid var(--accent-light)}
.hero-title{left:163px;top:74px;font-family:'Raleway',sans-serif;font-weight:500;font-size:36px;line-height:40px;color:var(--white)}
.hero-title .dots{color:var(--accent-light)}
.hero-btn{left:300px;top:149px;width:72px;height:20px;background:var(--white);color:var(--ink);font-family:'Lato',sans-serif;font-weight:700;font-size:8px;display:flex;align-items:center;justify-content:center}
.social-v{left:543px;top:46px;display:flex;flex-direction:column;gap:4px}

/* about */
.about{left:0;top:208px;width:565px;height:279px;background:var(--panel)}
.section-label{font-family:'Raleway',sans-serif;font-weight:500;font-size:12px;color:var(--accent)}
.section-label u{text-decoration:none;border-bottom:1px solid var(--ink);padding-bottom:1px}
.about-title{left:41px;top:42px;font-weight:700;font-size:19.5px;line-height:20px}
.about-copy{left:42px;top:92px;width:236px;font-size:10px;line-height:12px;color:var(--text)}
.years-box{left:108px;top:180px;width:78px;height:67px;border:2px solid var(--accent)}
.years-num{left:143px;top:190px;font-weight:500;font-size:44px;line-height:48px;color:var(--ink)}
.years-text{left:196px;top:190px;font-weight:400;font-size:12px;line-height:15.5px}
.years-text b{font-weight:400;color:var(--muted)}
.about-frame{left:330px;top:14px;width:128px;height:258px;border:2px solid var(--accent)}
.about-photo{left:355px;top:22px;width:164px;height:239px;background:linear-gradient(180deg,#8f8f8f 0%,#c4c4c4 55%,#9aa3a6 75%,#2b3232 100%)}

/* services */
.services{left:0;top:487px;width:565px;height:275px;background:var(--panel)}
.card{top:40px;width:181px;height:223px;overflow:hidden}
.card-photo{left:0;top:0;width:100%;height:100%}
.card-title{font-weight:700;font-size:15px;line-height:19px;color:var(--white)}
.card-copy{left:14px;top:68px;width:150px;font-family:'Lato',sans-serif;font-weight:700;font-size:6.5px;line-height:12px;color:var(--white)}
.see{left:118px;top:201px;font-family:'Lato',sans-serif;font-weight:700;font-size:7.5px;color:var(--white);display:flex;align-items:center;gap:3px}
.arrow{width:18px;height:18px;border-radius:50%;background:var(--white);box-shadow:0 1px 3px rgba(0,0,0,.25);display:flex;align-items:center;justify-content:center}

/* contact */
.contact{left:0;top:762px;width:565px;height:281px;background:var(--panel-alt)}
.contact-copy{left:49px;top:30px;width:460px;font-family:'Mulish',sans-serif;font-size:8px;line-height:15px;letter-spacing:.4px;color:var(--text)}
.field-label{font-family:'Mulish',sans-serif;font-size:10px;color:var(--accent);letter-spacing:.3px}
.field{left:121px;width:288px;background:var(--white);border:1px solid var(--accent);border-radius:2px;font-family:'Mulish',sans-serif;font-size:7.5px;color:var(--muted);padding:8px 15px;letter-spacing:.3px}
.send{left:321px;top:249px;width:84px;height:21px;border-radius:11px;background:var(--accent);color:var(--white);font-family:'Mulish',sans-serif;font-size:8px;letter-spacing:.3px;display:flex;align-items:center;justify-content:center}

/* footer */
.footer{left:0;top:1043px;width:565px;height:157px;background:var(--footer);color:var(--white)}
.footer-brand{left:48px;top:39px;display:flex;align-items:center;gap:9px;font-size:12px;letter-spacing:4px}
.footer-brand .brand-dot{width:28px;height:28px}
.links{font-family:'Raleway',sans-serif;font-weight:500;font-size:7.5px;line-height:14.5px}
.social-h{left:432px;top:41px;display:flex;gap:7px}
.copyright{left:0;top:141px;width:565px;text-align:center;font-weight:500;font-size:7.5px}
</style>
</head>
<body>
<div class="site">

  <header class="hero abs">
    <div class="hero-photo abs" role="img" aria-label="Black and white photo of a modern flat-roofed house at dusk with a pool in front"></div>
    <div class="brand abs"><span class="brand-dot"></span>KERROWMADE</div>
    <div class="call abs">CALL US: (+64) 2100 48 37 615</div>
    <svg class="abs" style="left:513px;top:9px" width="16" height="10" viewBox="0 0 16 10"><path d="M1 1h14M1 5h14M1 9h14" stroke="#fff" stroke-width="0.8"/></svg>
    <svg class="abs" style="left:542px;top:7px" width="13" height="13" viewBox="0 0 13 13"><circle cx="5.5" cy="5.5" r="4.5" fill="none" stroke="#fff" stroke-width="1"/><path d="M8.8 8.8L12.5 12.5" stroke="#fff" stroke-width="1.2"/></svg>
    <div class="social-v abs">
      <svg width="13" height="13"><circle cx="6.5" cy="6.5" r="6.5" fill="#fff"/></svg>
      <svg width="13" height="13"><circle cx="6.5" cy="6.5" r="6.5" fill="#fff"/></svg>
      <svg width="13" height="13" viewBox="0 0 13 13"><circle cx="6.5" cy="6.5" r="6.5" fill="#fff"/><rect x="3.3" y="4.2" width="6.4" height="4.6" fill="none" stroke="#555" stroke-width="0.9"/><path d="M3.3 4.2l3.2 2.6 3.2-2.6" fill="none" stroke="#555" stroke-width="0.9"/></svg>
    </div>
    <div class="hero-frame abs"></div>
    <h1 class="hero-title abs">WE Build For<br>You<span class="dots">...</span></h1>
    <div class="hero-btn abs">Get in touch</div>
  </header>

  <section class="about abs">
    <div class="section-label abs" style="left:46px;top:15px">About <u>Us</u></div>
    <h2 class="about-title abs">We are the Leader<br>in Architechural</h2>
    <p class="about-copy abs">Our vision is to build beautiful, efficient homes with the best building technologies available that our customers are proud to own.</p>
    <div class="years-box abs"></div>
    <div class="years-num abs">35</div>
    <div class="years-text abs"><b>W</b>orking<br><b>E</b>xperience<br><b>Y</b>ears</div>
    <div class="about-frame abs"></div>
    <div class="about-photo abs" role="img" aria-label="Photo of white gabled houses with dark roofs against a grey sky"></div>
  </section>

  <section class="services abs">
    <div class="section-label abs" style="left:48px;top:6px">Our <u>Services</u></div>
    <article class="card abs" style="left:0">
      <div class="card-photo abs" role="img" aria-label="Photo of a white modern house under a pale sky" style="background:linear-gradient(180deg,#a9adb0 0%,#d4d6d7 45%,#ebebeb 75%,#bdbfc0 100%)"></div>
      <div class="card-title abs" style="left:20px;top:173px">Design and<br>Build</div>
    </article>
    <article class="card abs" style="left:193px;top:38px;height:224px">
      <div class="card-photo abs" role="img" aria-label="Photo of a house interior lit at night" style="background:linear-gradient(180deg,#181818 0%,#222 45%,#2c2c2c 70%,#151515 100%)"></div>
      <div class="card-title abs" style="left:15px;top:20px">Renovation and<br>Addtions</div>
      <p class="card-copy abs">Lorem ipsum dolor sit amet, consectetur adipisicing elit, sed do eiusmod tempor incididunt ut labore et dolore magna aliqua. Ut enim ad minim veniam, quis nostrud exercitation</p>
      <div class="card-title abs" style="left:20px;top:175px;opacity:.18">Renovation and<br>Addtions</div>
      <div class="see abs">See Project <svg width="5" height="8" viewBox="0 0 5 8"><path d="M1 1l3 3-3 3" fill="none" stroke="#fff" stroke-width="1.2"/></svg></div>
    </article>
    <article class="card abs" style="left:385px">
      <div class="card-photo abs" role="img" aria-label="Photo of a white modern apartment building" style="background:linear-gradient(180deg,#c6c8c9 0%,#e2e3e4 40%,#d0d1d2 70%,#a2a4a5 100%)"></div>
      <div class="card-title abs" style="left:29px;top:173px">Project<br>Mangaement</div>
    </article>
    <div class="arrow abs" style="left:-7px;top:129px"><svg width="7" height="11" viewBox="0 0 7 11"><path d="M5.5 1L1.5 5.5l4 4.5" fill="none" stroke="#4a4a4a" stroke-width="1.6"/></svg></div>
    <div class="arrow abs" style="left:555px;top:126px"><svg width="7" height="11" viewBox="0 0 7 11"><path d="M1.5 1l4 4.5-4 4.5" fill="none" stroke="#4a4a4a" stroke-width="1.6"/></svg></div>
  </section>

  <section class="contact abs">
    <div class="section-label abs" style="left:50px;top:8px">Contact <u>Us</u></div>
    <p class="contact-copy abs">We’d love to hear about your building project and discuss how Kerrowmade can help you design and build your dream home smarter.</p>
    <div class="field-label abs" style="left:60px;top:84px">Name</div>
    <div class="field abs" style="top:80px;height:27px">Enter Your Name</div>
    <div class="field-label abs" style="left:60px;top:120px">Email</div>
    <div class="field abs" style="top:114px;height:27px">Enter Your Email</div>
    <div class="field-label abs" style="left:60px;top:152px">Message</div>
    <div class="field abs" style="top:146px;height:93px">Enter Your Message</div>
    <div class="send abs">Get in Touch</div>
  </section>

  <footer class="footer abs">
    <div class="footer-brand abs"><span class="brand-dot"></span>KERROWMADE</div>
    <div class="links abs" style="left:226px;top:38px">Site Map<br>Terms &amp; Condition<br>Privacy Policy<br>Help</div>
    <div class="links abs" style="left:344px;top:38px">Our Location<br>About Us<br>Career<br>Contact Us</div>
    <div class="social-h abs">
      <svg width="13" height="13"><circle cx="6.5" cy="6.5" r="6.5" fill="#fff"/></svg>
      <svg width="13" height="13" viewBox="0 0 13 13"><circle cx="6.5" cy="6.5" r="6.5" fill="#fff"/><rect x="3.3" y="4.2" width="6.4" height="4.6" fill="none" stroke="#1f1f1f" stroke-width="0.9"/><path d="M3.3 4.2l3.2 2.6 3.2-2.6" fill="none" stroke="#1f1f1f" stroke-width="0.9"/></svg>
      <svg width="13" height="13"><circle cx="6.5" cy="6.5" r="6.5" fill="#fff"/></svg>
      <svg width="13" height="13"><circle cx="6.5" cy="6.5" r="6.5" fill="#fff"/></svg>
    </div>
    <div class="copyright abs">© Copyright KERROWMADE All Right Reserved</div>
  </footer>

</div>
</body>
</html>
```